Urgent Care opening in Wauchula Florida

we need postcards for our Urgent care that we are opening in Wauchula Florida. We are going to send these postcards in the backpacks for children when the get back to school. I am attaching an idea we foundAddress: 482 N elm lane Wauchula Florida 33873phone # 863-773-4700Hours of business M-F 9-5Saturday 9-5Hours may still changeAlso this design will be used for the banner

Target Market(s)

rural community

Industry/Entity Type

Medical

Other font styles liked:
• any suggested by designer

Requirements
Must have
• see attached file for type of services needed
Nice to have
• see attached file need to have map where office is, services of urgent care

```html
<!DOCTYPE html>
<html lang="en">
<head>
<meta charset="utf-8">
<title>Urgent Care Postcard – Wauchula Florida</title>
<link href="https://fonts.googleapis.com/css2?family=Open+Sans:wght@400;600;700;800&family=Oswald:wght@500;600&display=swap" rel="stylesheet">
<style>
  :root{
    --bg:#ececec;
    --card:#ffffff;
    --card-shade:#eef0f3;
    --red:#e0262a;
    --blue:#3a67b8;
    --blue-dark:#2a4f96;
    --blue-light:#6d8fd0;
    --green:#7cbf2f;
    --green-dark:#5a9a1c;
    --ink:#2f3b4c;
    --grey:#9aa3ad;
  }
  *{box-sizing:border-box;margin:0;padding:0}
  html,body{width:900px;height:1200px;overflow:hidden;background:var(--bg)}
  body{position:relative;font-family:"Open Sans",Arial,sans-serif;color:var(--ink)}

  .postcard{position:absolute;left:66px;width:768px;background:var(--card);overflow:hidden;
    box-shadow:0 6px 18px rgba(0,0,0,.18)}
  .postcard--front{top:36px;height:528px;background:linear-gradient(180deg,#fff 0%,var(--card-shade) 100%)}
  .postcard--back{top:612px;height:552px}

  /* front */
  .header{position:absolute;top:14px;left:0;width:100%;height:70px}
  .header svg{position:absolute;inset:0}
  .header__title{position:absolute;left:0;right:0;top:12px;text-align:center;
    font-family:"Oswald",Arial,sans-serif;font-weight:600;font-size:38px;color:var(--red);letter-spacing:.5px}
  .header__title span{background:var(--card);padding:0 14px}

  .opening{position:absolute;left:36px;top:100px;width:360px;height:96px;background:var(--blue)}
  .opening__lead{color:#fff;font-weight:700;font-size:25px;padding:8px 16px 0}
  .opening__city{position:absolute;left:12px;bottom:8px;background:#fff;color:var(--blue-dark);
    font-weight:800;font-size:27px;padding:2px 12px;border-right:10px solid var(--green)}

  .photo{position:absolute;right:0;top:196px;width:400px;height:332px;
    background:linear-gradient(135deg,#dfe7f1 0%,#c6d3e4 55%,#f3f5f8 100%)}
  .swoosh{position:absolute;left:300px;top:180px;width:170px;height:348px}

  .hours{position:absolute;left:36px;top:262px;width:312px;height:180px;background:var(--blue-dark);padding:12px 18px}
  .hours__time{color:#fff;font-weight:800;font-size:30px;line-height:1.15;white-space:nowrap}
  .hours__note{color:var(--green);font-weight:800;font-size:26px;line-height:1.2}
  .hours__days{color:#fff;font-weight:700;font-size:26px;line-height:1.18;text-transform:uppercase}
  .address{position:absolute;left:36px;top:448px;width:312px;height:72px;background:var(--blue-light);
    color:#fff;font-size:20px;font-weight:600;line-height:1.3;padding:6px 18px}

  /* back */
  .ribbon{position:absolute;left:0;top:30px;width:330px;height:62px;background:var(--green);
    color:#fff;font-weight:800;font-size:16px;line-height:1.3;padding:10px 20px 0 32px;text-transform:uppercase;
    clip-path:polygon(0 0,100% 0,92% 100%,0 100%)}
  .services{position:absolute;left:38px;top:108px;list-style:none}
  .services li{display:flex;align-items:flex-start;gap:10px;font-size:18px;line-height:24px;color:var(--ink);max-width:330px}
  .services svg{flex:none;margin-top:4px}
  .divider{position:absolute;left:384px;top:40px;width:1px;height:480px;background:#d3d8de}
  .stamp{position:absolute;right:84px;top:72px;width:90px;height:84px;border:3px solid #111}
  .phone{position:absolute;left:30px;bottom:24px;width:250px;height:48px;background:var(--green);
    border-radius:24px;display:flex;align-items:center;gap:14px;padding-left:6px;color:#fff;font-weight:800;font-size:24px}
  .phone__icon{width:38px;height:38px;border-radius:50%;background:#fff;display:flex;align-items:center;justify-content:center}
</style>
</head>
<body>

<section class="postcard postcard--front">
  <div class="header">
    <svg width="768" height="70" viewBox="0 0 768 70">
      <polyline points="0,36 200,36 214,14 226,58 238,24 248,36 520,36 532,14 544,58 556,24 566,36 768,36"
        fill="none" stroke="var(--grey)" stroke-width="3"/>
    </svg>
    <div class="header__title"><span>Urgent care</span></div>
  </div>

  <div class="opening">
    <p class="opening__lead">We are opening in</p>
    <p class="opening__city">Wauchula Florida</p>
  </div>

  <div class="photo" role="img" aria-label="Photo of a medical team of doctors and nurses reviewing notes at a desk"></div>
  <svg class="swoosh" viewBox="0 0 170 348">
    <path d="M120,0 C40,90 40,250 110,348 L170,348 L170,0 Z" fill="var(--card-shade)"/>
    <path d="M120,0 C40,90 40,250 110,348" fill="none" stroke="var(--green)" stroke-width="8"/>
    <path d="M150,0 C80,90 80,250 140,348" fill="none" stroke="var(--blue)" stroke-width="5"/>
  </svg>

  <div class="hours">
    <p class="hours__time">9:00am - 5:00pm</p>
    <p class="hours__note">(MON - FRI)</p>
    <p class="hours__days">· Saturday<br>&nbsp;&nbsp;9:00am - 5:00pm</p>
  </div>
  <div class="address">482 N elm lane<br>Wauchula Florida 33873</div>
</section>

<section class="postcard postcard--back">
  <div class="ribbon">Prompt &amp; courteous treatment for:</div>
  <ul class="services">
    <li><svg width="16" height="16" viewBox="0 0 16 16"><rect x="1" y="1" width="14" height="14" fill="none" stroke="var(--blue)" stroke-width="1.5"/><path d="M4 8l3 3 6-7" fill="none" stroke="var(--blue)" stroke-width="2"/></svg>General Medical Care</li>
    <li><svg width="16" height="16" viewBox="0 0 16 16"><rect x="1" y="1" width="14" height="14" fill="none" stroke="var(--blue)" stroke-width="1.5"/><path d="M4 8l3 3 6-7" fill="none" stroke="var(--blue)" stroke-width="2"/></svg>Colds</li>
    <li><svg width="16" height="16" viewBox="0 0 16 16"><rect x="1" y="1" width="14" height="14" fill="none" stroke="var(--blue)" stroke-width="1.5"/><path d="M4 8l3 3 6-7" fill="none" stroke="var(--blue)" stroke-width="2"/></svg>Sore Throats</li>
    <li><svg width="16" height="16" viewBox="0 0 16 16"><rect x="1" y="1" width="14" height="14" fill="none" stroke="var(--blue)" stroke-width="1.5"/><path d="M4 8l3 3 6-7" fill="none" stroke="var(--blue)" stroke-width="2"/></svg>Influenza</li>
    <li><svg width="16" height="16" viewBox="0 0 16 16"><rect x="1" y="1" width="14" height="14" fill="none" stroke="var(--blue)" stroke-width="1.5"/><path d="M4 8l3 3 6-7" fill="none" stroke="var(--blue)" stroke-width="2"/></svg>Ear Infections</li>
    <li><svg width="16" height="16" viewBox="0 0 16 16"><rect x="1" y="1" width="14" height="14" fill="none" stroke="var(--blue)" stroke-width="1.5"/><path d="M4 8l3 3 6-7" fill="none" stroke="var(--blue)" stroke-width="2"/></svg>Lacerations</li>
    <li><svg width="16" height="16" viewBox="0 0 16 16"><rect x="1" y="1" width="14" height="14" fill="none" stroke="var(--blue)" stroke-width="1.5"/><path d="M4 8l3 3 6-7" fill="none" stroke="var(--blue)" stroke-width="2"/></svg>Foreign Body Removals</li>
    <li><svg width="16" height="16" viewBox="0 0 16 16"><rect x="1" y="1" width="14" height="14" fill="none" stroke="var(--blue)" stroke-width="1.5"/><path d="M4 8l3 3 6-7" fill="none" stroke="var(--blue)" stroke-width="2"/></svg>Burns</li>
    <li><svg width="16" height="16" viewBox="0 0 16 16"><rect x="1" y="1" width="14" height="14" fill="none" stroke="var(--blue)" stroke-width="1.5"/><path d="M4 8l3 3 6-7" fill="none" stroke="var(--blue)" stroke-width="2"/></svg>Broken Bones</li>
    <li><svg width="16" height="16" viewBox="0 0 16 16"><rect x="1" y="1" width="14" height="14" fill="none" stroke="var(--blue)" stroke-width="1.5"/><path d="M4 8l3 3 6-7" fill="none" stroke="var(--blue)" stroke-width="2"/></svg>Minor Surgical Procedures,</li>
    <li><svg width="16" height="16" viewBox="0 0 16 16"><rect x="1" y="1" width="14" height="14" fill="none" stroke="var(--blue)" stroke-width="1.5"/><path d="M4 8l3 3 6-7" fill="none" stroke="var(--blue)" stroke-width="2"/></svg>Physical Exams</li>
    <li><svg width="16" height="16" viewBox="0 0 16 16"><rect x="1" y="1" width="14" height="14" fill="none" stroke="var(--blue)" stroke-width="1.5"/><path d="M4 8l3 3 6-7" fill="none" stroke="var(--blue)" stroke-width="2"/></svg>Immunizations</li>
    <li><svg width="16" height="16" viewBox="0 0 16 16"><rect x="1" y="1" width="14" height="14" fill="none" stroke="var(--blue)" stroke-width="1.5"/><path d="M4 8l3 3 6-7" fill="none" stroke="var(--blue)" stroke-width="2"/></svg>Workers Compensation Evaluation &amp; Treatment</li>
  </ul>

  <div class="divider"></div>
  <div class="stamp"></div>

  <div class="phone">
    <span class="phone__icon">
      <svg width="22" height="22" viewBox="0 0 24 24"><path d="M6.6 10.8a15.1 15.1 0 006.6 6.6l2.2-2.2c.3-.3.7-.4 1-.2 1.1.4 2.3.6 3.6.6.6 0 1 .4 1 1V20c0 .6-.4 1-1 1A17 17 0 013 4c0-.6.4-1 1-1h3.5c.6 0 1 .4 1 1 0 1.3.2 2.5.6 3.6.1.3 0 .7-.2 1z" fill="var(--green-dark)"/></svg>
    </span>
    841-362-5097
  </div>
</section>

</body>
</html>
```